3 Politically Incorrect Greeting Cards

I would like to see some clean, colorful, and modern designs for 3 "politically incorrect" greeting cards aimed at young, single, successful women. I would like them to say:

Card 1: " Congratulations on not marrying the wrong person"
Card 2: " Congratulations on buying a house without a husband"
Card 3: " Thank you for not forgetting about me now that you have a boyfriend"

My initial thought was to have a white background with simple black writing, but I think a colorful background with a white text box in the middle might be more appropriate. I can't imagine the cards having any images/icons on them, but I'm open to suggestions if you think it would improve on the design. You guys are likely more creative than I am.

I've included a couple pics of looks I like - but like I said - I'm open to suggestions and what I like may not be appropriate for these cards. All the cards can have a similar esthetic or theme (maybe the same fonts but different colors or different color florals in each) or they can be completely different.

Target Market(s)

Young, single, successful women mid-20s to mid 40's.

Font styles to use
Serif
Sans Serif
Other font styles liked:
• Watercolour lettering maybe

Colors

Designer to choose colors to be used in the design.

Requirements
Must have
• Clean, colorful, bright, professional looking. The right tone for the message.
• I think the message is bold so the writing and colors have to be as well. I have included examples of ideas I like.
Nice to have
• Images, illustrations, icons, maybe patterns or some decorative details. Something to make the card more interesting than just the words (like the blue background with black letters one I made). I like a bright pattern with a white box in the center with the text.
Should not have
• Special effects, galaxy pictures, ugly images, bland colors.

```html
<!DOCTYPE html>
<html lang="en">
<head>
<meta charset="utf-8">
<title>Greeting Card Set</title>
<link rel="stylesheet" href="https://fonts.googleapis.com/css2?family=Open+Sans:wght@400&family=Roboto+Condensed:ital,wght@1,300&display=swap">
<style>
  :root {
    --page: #ffffff;
    --plum: #4f2d4d;
    --plum-title: #f1e0ea;
    --plum-note: #a4849f;
    --navy: #27364b;
    --navy-title: #e5edf0;
    --navy-note: #8b97a7;
    --blush: #e0aecb;
    --blush-title: #fcf3ee;
    --blush-note: #f6e8e6;
  }
  html, body {
    margin: 0;
    padding: 0;
    width: 1200px;
    height: 1200px;
    overflow: hidden;
    background: var(--page);
  }
  .card-stack {
    position: absolute;
    left: 366px;
    top: 61px;
    width: 492px;
  }
  .card {
    position: relative;
    height: 357.6px;
    text-align: center;
  }
  .card--plum { background: var(--plum); }
  .card--navy { background: var(--navy); }
  .card--blush { background: var(--blush); }
  .card__message {
    position: absolute;
    left: 0;
    right: 0;
    top: 157px;
    margin: 0;
  }
  .card__title {
    display: block;
    font-family: "Open Sans", sans-serif;
    font-weight: 400;
    font-size: 21px;
    line-height: 22px;
    letter-spacing: 0.06em;
  }
  .card__note {
    display: block;
    font-family: "Roboto Condensed", sans-serif;
    font-style: italic;
    font-weight: 300;
    font-size: 10.5px;
    line-height: 12px;
    letter-spacing: 0.14em;
    margin-top: 0;
  }
  .card--plum .card__title { color: var(--plum-title); }
  .card--plum .card__note { color: var(--plum-note); }
  .card--navy .card__title { color: var(--navy-title); }
  .card--navy .card__note { color: var(--navy-note); }
  .card--blush .card__title { color: var(--blush-title); letter-spacing: 0.2em; }
  .card--blush .card__note { color: var(--blush-note); letter-spacing: 0.1em; }
</style>
</head>
<body>
  <main class="card-stack">
    <section class="card card--plum">
      <p class="card__message">
        <span class="card__title">CONGRATULATIONS</span>
        <span class="card__note">on not marrying the wrong person</span>
      </p>
    </section>
    <section class="card card--navy">
      <p class="card__message">
        <span class="card__title">CONGRATULATIONS</span>
        <span class="card__note">on buying a house without a husband</span>
      </p>
    </section>
    <section class="card card--blush">
      <p class="card__message">
        <span class="card__title">THANK YOU</span>
        <span class="card__note">for not forgetting about me now that you have a boyfriend</span>
      </p>
    </section>
  </main>
</body>
</html>
```